Presentation Folder Mesa Coverage Advisors

I would like a two sided presentation folder 9" wide x 12" tall for our benefits/ insurance company. It must be professional and instill confidence in our customers. PixelGuild designed our logo which must be included. Our website is www.mcvllc.org The logo on the website is the old one as a new website is about to launch. The contact information and address are correct on the website. We provide health, disability and other benefits to employers and will use this when making presentations about plans and renewals. I have been told to put this as stationery from someone at PixelGuild but it is not stationery. Please feel free to email me if you have questions.

Reason: My committee meets Oct. 17.

```html
<!DOCTYPE html>
<html lang="en">
<head>
<meta charset="utf-8">
<title>Mesa Coverage Advisors – Presentation Folder</title>
<link href="https://fonts.googleapis.com/css2?family=Cinzel:wght@600&family=Questrial&display=swap" rel="stylesheet">
<style>
  :root {
    --stage: #c9c9c9;
    --paper: #ffffff;
    --folder-inside: #eceef3;
    --pattern-tone: #d9dce8;
    --navy: #17196e;
    --navy-deep: #0f1150;
    --gold: #d49a2a;
    --ink-light: #ffffff;
  }
  * { box-sizing: border-box; margin: 0; padding: 0; }
  html, body { width: 1200px; height: 686px; overflow: hidden; }
  body {
    background: var(--stage);
    font-family: "Questrial", "Century Gothic", sans-serif;
    position: relative;
  }

  /* open folder interior */
  .folder-panel {
    position: absolute;
    top: 52px;
    height: 598px;
    background: var(--folder-inside);
  }
  .folder-panel--left { left: 290px; width: 425px; }
  .folder-panel--right { left: 715px; width: 420px; }
  .folder-pattern {
    position: absolute;
    inset: 0;
    background: linear-gradient(180deg, var(--pattern-tone), var(--folder-inside));
  }
  .folder-spine {
    position: absolute;
    left: 714px; top: 52px;
    width: 2px; height: 598px;
    background: #cfd2dc;
  }

  .pocket { position: absolute; left: 715px; top: 52px; }

  /* wordmark */
  .wordmark {
    display: flex;
    align-items: center;
    gap: 10px;
  }
  .wordmark__square {
    width: 30px; height: 30px;
    background: var(--navy);
    flex: none;
  }
  .wordmark__name {
    font-family: "Cinzel", serif;
    font-weight: 600;
    color: var(--navy);
    line-height: 1.05;
  }

  /* letterhead */
  .letterhead {
    position: absolute;
    left: 72px; top: 67px;
    width: 396px; height: 569px;
    background: var(--paper);
    box-shadow: 0 2px 6px rgba(0,0,0,.15);
  }
  .letterhead .wordmark { position: absolute; left: 40px; top: 40px; }
  .letterhead .wordmark__name { font-size: 13px; }
  .letterhead__footer {
    position: absolute;
    left: 0; bottom: 0;
    width: 100%; height: 32px;
    background: var(--navy);
    border-top: 5px solid var(--gold);
    color: var(--ink-light);
    font-size: 5.5px;
    display: flex;
    align-items: center;
    padding: 0 32px;
    gap: 30px;
  }
  .letterhead__footer .company { width: 160px; line-height: 1.6; }
  .contact-col { line-height: 1.6; }
  .contact-line { display: flex; align-items: center; gap: 4px; }
  .icon { width: 7px; height: 7px; flex: none; }

  /* business card */
  .business-card {
    position: absolute;
    left: 773px; top: 507px;
    width: 167px; height: 100px;
    background: var(--paper);
    display: flex;
    align-items: center;
    justify-content: center;
  }
  .business-card .wordmark { gap: 6px; }
  .business-card .wordmark__square { width: 20px; height: 20px; }
  .business-card .wordmark__name { font-size: 8.5px; }

  /* pocket contact */
  .pocket-contact {
    position: absolute;
    left: 985px; top: 509px;
    color: var(--ink-light);
    font-size: 6px;
    line-height: 1.6;
  }
  .pocket-contact .group { margin-bottom: 8px; }
  .pocket-contact .icon { width: 8px; height: 8px; }
</style>
</head>
<body>

  <div class="folder-panel folder-panel--left">
    <div class="folder-pattern" role="img" aria-label="Faint repeating brand monogram pattern on the folder interior"></div>
  </div>
  <div class="folder-panel folder-panel--right">
    <div class="folder-pattern" role="img" aria-label="Faint repeating brand monogram pattern on the folder interior"></div>
  </div>
  <div class="folder-spine"></div>

  <svg class="pocket" width="430" height="600" viewBox="0 0 430 600" aria-hidden="true">
    <defs>
      <linearGradient id="pocketFill" x1="0" y1="0" x2="1" y2="1">
        <stop offset="0" stop-color="#1c1f82"/>
        <stop offset="1" stop-color="#10125a"/>
      </linearGradient>
    </defs>
    <!-- vertical side flap -->
    <path d="M330 40 Q330 20 350 14 L410 6 L420 590 L310 590 L310 440 L330 440 Z" fill="url(#pocketFill)"/>
    <!-- horizontal bottom pocket -->
    <path d="M18 434 L382 434 Q400 436 402 452 L425 598 L3 598 Z" fill="url(#pocketFill)"/>
    <path d="M18 434 L382 434" stroke="#2a2e96" stroke-width="1"/>
  </svg>

  <div class="letterhead">
    <div class="wordmark">
      <span class="wordmark__square"></span>
      <span class="wordmark__name">Mesa Coverage<br>Advisors</span>
    </div>
    <div class="letterhead__footer">
      <div class="company">MESA COVERAGE ADVISORS, LLC<br>1820 E Saguaro Way, Suite 310, Mesa, AZ 85203-4410</div>
      <div class="contact-col">
        <div class="contact-line">
          <svg class="icon" viewBox="0 0 10 10"><circle cx="5" cy="5" r="5" fill="var(--gold)"/><path d="M3 2.5l1 1-.6.8a4 4 0 0 0 2.3 2.3l.8-.6 1 1-.8.8A5 5 0 0 1 2.2 3.3z" fill="var(--navy)"/></svg>480-555-0142
        </div>
        <div class="contact-line">
          <svg class="icon" viewBox="0 0 10 10"><circle cx="5" cy="5" r="5" fill="var(--gold)"/><rect x="2.8" y="3.2" width="4.4" height="3.6" fill="var(--navy)"/></svg>480-555-0178
        </div>
      </div>
      <div class="contact-col">
        <div class="contact-line">
          <svg class="icon" viewBox="0 0 10 10"><circle cx="5" cy="5" r="5" fill="var(--gold)"/><rect x="2.5" y="3.2" width="5" height="3.6" fill="var(--navy)"/></svg>info@mcvllc.org
        </div>
        <div class="contact-line">
          <svg class="icon" viewBox="0 0 10 10"><circle cx="5" cy="5" r="5" fill="var(--gold)"/><circle cx="5" cy="5" r="2.6" fill="none" stroke="var(--navy)" stroke-width="1"/></svg>www.mcvllc.org
        </div>
      </div>
    </div>
  </div>

  <div class="business-card">
    <div class="wordmark">
      <span class="wordmark__square"></span>
      <span class="wordmark__name">Mesa Coverage<br>Advisors</span>
    </div>
  </div>

  <div class="pocket-contact">
    <div class="group">1820 E Saguaro Way, Suite 310<br>Mesa, AZ 85203-4410</div>
    <div class="group">
      <div class="contact-line"><svg class="icon" viewBox="0 0 10 10"><circle cx="5" cy="5" r="5" fill="var(--gold)"/><path d="M3 2.5l1 1-.6.8a4 4 0 0 0 2.3 2.3l.8-.6 1 1-.8.8A5 5 0 0 1 2.2 3.3z" fill="var(--navy)"/></svg>480-555-0142</div>
      <div class="contact-line"><svg class="icon" viewBox="0 0 10 10"><circle cx="5" cy="5" r="5" fill="var(--gold)"/><rect x="2.8" y="3.2" width="4.4" height="3.6" fill="var(--navy)"/></svg>480-555-0178</div>
    </div>
    <div class="group">
      <div class="contact-line"><svg class="icon" viewBox="0 0 10 10"><circle cx="5" cy="5" r="5" fill="var(--gold)"/><rect x="2.5" y="3.2" width="5" height="3.6" fill="var(--navy)"/></svg>info@mcvllc.org</div>
      <div class="contact-line"><svg class="icon" viewBox="0 0 10 10"><circle cx="5" cy="5" r="5" fill="var(--gold)"/><circle cx="5" cy="5" r="2.6" fill="none" stroke="var(--navy)" stroke-width="1"/></svg>www.mcvllc.org</div>
    </div>
  </div>

</body>
</html>
```